Need Flyer for Our Real estate Agency

Need to run General Campaign for our agency with Start of New Year as our theme ..Must have an agent's picture on the DL..
Address:
9 / 386Barwin rd, Carrowvale VIC 3041
Ph:03 9142 7305
email:info@koridanrealestate.example.au
www.koridanrealestate.example.au
Something like as attached picture..
Target Market(s)
Home Buyers
Industry/Entity Type
Real Estate Agent
Requirements
Must have
- Our Logo Colours

```html
<!DOCTYPE html>
<html lang="en">
<head>
<meta charset="utf-8">
<title>Koridan – DL Flyer</title>
<link rel="stylesheet" href="https://fonts.googleapis.com/css2?family=Crimson+Pro:wght@500&family=Open+Sans:wght@400;600&display=swap">
<style>
  :root {
    --navy: #121c55;
    --red: #8b1428;
    --tagline-red: #a01a2e;
    --white: #ffffff;
    --page: #e4e5e8;
    --serif: "Crimson Pro", Georgia, serif;
    --sans: "Open Sans", Arial, sans-serif;
  }
  * { margin: 0; padding: 0; box-sizing: border-box; }
  html, body { width: 1200px; height: 1108px; overflow: hidden; }
  body { background: var(--page); position: relative; font-family: var(--sans); }

  .card {
    position: absolute; left: 50px; width: 1100px; height: 516px;
    overflow: hidden; background: var(--navy);
    box-shadow: 0 4px 10px rgba(0,0,0,0.25);
  }
  .card--front { top: 25px; }
  .card--back { top: 567px; }
  .card__shapes { position: absolute; inset: 0; width: 100%; height: 100%; }

  .brand-name {
    position: absolute; font-family: var(--serif); font-weight: 500;
    color: var(--white); font-size: 54px; letter-spacing: 6px;
    transform: translateX(-50%); white-space: nowrap; line-height: 1;
  }
  .card--front .brand-name { left: 860px; top: 130px; }
  .card--back .brand-name { left: 242px; top: 138px; }

  .tagline {
    position: absolute; left: 860px; top: 228px; transform: translateX(-50%);
    font-family: var(--serif); font-weight: 500; color: var(--tagline-red);
    font-size: 54px; line-height: 66px; text-align: center; white-space: nowrap;
  }

  .appraisal {
    position: absolute; right: 330px; top: 370px; text-align: right;
    color: var(--white); font-size: 24px; line-height: 35px; white-space: nowrap;
  }
  .appraisal strong { font-weight: 600; }
  .appraisal__divider {
    position: absolute; left: 796px; top: 374px; width: 2px; height: 64px;
    background: var(--white);
  }
  .front-phone {
    position: absolute; left: 818px; top: 388px; display: flex; align-items: center;
    gap: 8px; color: var(--white); font-size: 29px; letter-spacing: 3px; white-space: nowrap;
  }

  .web-bar {
    position: absolute; display: flex; align-items: center; gap: 8px;
    color: var(--white); font-size: 17px; letter-spacing: 3.5px; white-space: nowrap;
  }
  .card--front .web-bar { left: 554px; top: 477px; }
  .card--back .web-bar { left: 29px; top: 479px; }

  .services {
    position: absolute; left: 33px; top: 241px; display: flex; align-items: center;
    gap: 18px; font-family: var(--serif); font-weight: 500; color: var(--white);
    font-size: 27px; letter-spacing: 0.5px; white-space: nowrap;
  }
  .services__dot { width: 8px; height: 8px; border-radius: 50%; background: var(--red); }

  .contact-list { position: absolute; left: 33px; top: 318px; list-style: none; }
  .contact-list__item {
    display: flex; align-items: center; gap: 12px; height: 43px;
    color: var(--white); font-size: 26px; white-space: nowrap;
  }
  .icon { flex: none; fill: var(--white); }
</style>
</head>
<body>

<section class="card card--front" aria-label="Flyer front">
  <svg class="card__shapes" viewBox="0 0 1335 627" preserveAspectRatio="none">
    <defs>
      <linearGradient id="agentTone" x1="0" y1="0" x2="0" y2="1">
        <stop offset="0" stop-color="#f1f2f4"/>
        <stop offset="0.55" stop-color="#e2e4e8"/>
        <stop offset="1" stop-color="#3a4478"/>
      </linearGradient>
    </defs>
    <polygon points="0,0 547,0 714,295 527,627 0,627" fill="url(#agentTone)" role="img" aria-label="Portrait photo of the agent in a navy suit"/>
    <polygon points="547,0 585,0 750,295 567,627 527,627 714,295" fill="#8b1428"/>
    <polygon points="612,568 1335,568 1335,627 577,627" fill="#8b1428"/>
  </svg>

  <div class="brand-name">KORIDAN</div>

  <p class="tagline">Your New Year,<br>Your New Home</p>

  <p class="appraisal"><strong>Call Arjun Kalra</strong><br>for a <strong>free Appraisal</strong></p>
  <span class="appraisal__divider"></span>
  <p class="front-phone">
    <svg class="icon" width="24" height="24" viewBox="0 0 24 24"><path d="M6.6 10.8a15.1 15.1 0 0 0 6.6 6.6l2.2-2.2c.3-.3.7-.4 1-.2 1.1.4 2.3.6 3.6.6.6 0 1 .4 1 1V20c0 .6-.4 1-1 1C10.6 21 3 13.4 3 4c0-.6.4-1 1-1h3.5c.6 0 1 .4 1 1 0 1.3.2 2.5.6 3.6.1.3 0 .7-.2 1z"/></svg>
    03 9142 7305
  </p>

  <p class="web-bar">Visit us
    <svg width="16" height="16" viewBox="0 0 24 24" fill="none" stroke="#fff" stroke-width="2"><circle cx="12" cy="12" r="10"/><path d="M2 12h20M12 2c3 3 3 17 0 20M12 2c-3 3-3 17 0 20"/></svg>
    www.koridanrealestate.example.au</p>
</section>

<section class="card card--back" aria-label="Flyer back">
  <svg class="card__shapes" viewBox="0 0 1335 627" preserveAspectRatio="none">
    <defs>
      <linearGradient id="homeTone" x1="0" y1="0" x2="0" y2="1">
        <stop offset="0" stop-color="#8c80b9"/>
        <stop offset="0.2" stop-color="#c99ca9"/>
        <stop offset="0.45" stop-color="#a4503b"/>
        <stop offset="0.7" stop-color="#b9b2a8"/>
        <stop offset="1" stop-color="#5d7a37"/>
      </linearGradient>
    </defs>
    <polygon points="782,0 1335,0 1335,627 807,627 622,292" fill="url(#homeTone)" role="img" aria-label="Photo of a two-storey brick family home at dusk"/>
    <polygon points="739,0 782,0 622,292 807,627 765,627 579,292" fill="#8b1428"/>
    <polygon points="0,569 708,569 742,627 0,627" fill="#8b1428"/>
  </svg>

  <div class="brand-name">KORIDAN</div>

  <p class="services">BUYING <span class="services__dot"></span> SELLING <span class="services__dot"></span> LEASING</p>

  <ul class="contact-list">
    <li class="contact-list__item">
      <svg class="icon" width="22" height="22" viewBox="0 0 24 24"><path d="M6.6 10.8a15.1 15.1 0 0 0 6.6 6.6l2.2-2.2c.3-.3.7-.4 1-.2 1.1.4 2.3.6 3.6.6.6 0 1 .4 1 1V20c0 .6-.4 1-1 1C10.6 21 3 13.4 3 4c0-.6.4-1 1-1h3.5c.6 0 1 .4 1 1 0 1.3.2 2.5.6 3.6.1.3 0 .7-.2 1z"/></svg>
      03 9142 7305
    </li>
    <li class="contact-list__item">
      <svg class="icon" width="22" height="22" viewBox="0 0 24 24"><path d="M2 5h20v3l-10 6L2 8z"/><path d="M2 10l10 6 10-6v9H2z"/></svg>
      info@koridanrealestate.example.au
    </li>
    <li class="contact-list__item">
      <svg class="icon" width="22" height="22" viewBox="0 0 24 24"><path d="M12 2a7 7 0 0 0-7 7c0 5 7 13 7 13s7-8 7-13a7 7 0 0 0-7-7zm0 9.5A2.5 2.5 0 1 1 12 6.5a2.5 2.5 0 0 1 0 5z"/></svg>
      9 / 386Barwin rd, Carrowvale VIC 3041
    </li>
  </ul>

  <p class="web-bar">Visit us
    <svg width="16" height="16" viewBox="0 0 24 24" fill="none" stroke="#fff" stroke-width="2"><circle cx="12" cy="12" r="10"/><path d="M2 12h20M12 2c3 3 3 17 0 20M12 2c-3 3-3 17 0 20"/></svg>
    www.koridanrealestate.example.au</p>
</section>

</body>
</html>
```